Business cards for law firm with global theme

I'd like business cards with contact info for two offices. They should include the colors and font of the new logo design, which is a stylized globe with an "F" in it. The feel should be very modern and professional.

```html
<!DOCTYPE html>
<html lang="en">
<head>
<meta charset="utf-8">
<title>Marlowe Law — Business Cards</title>
<link href="https://fonts.googleapis.com/css2?family=Montserrat:wght@400;500;700;800&display=swap" rel="stylesheet">
<style>
  :root {
    --navy: #143f74;
    --navy-deep: #0f3566;
    --sky: #29a9e1;
    --ink: #2b2f36;
    --paper: #ffffff;
    --backdrop: #e9ecf0;
  }
  * { box-sizing: border-box; margin: 0; padding: 0; }
  html, body {
    width: 1200px; height: 912px; overflow: hidden;
    background: var(--backdrop);
    font-family: "Montserrat", sans-serif;
  }
  .sheet {
    position: relative; width: 1200px; height: 912px;
    display: flex; align-items: center; justify-content: center; gap: 40px;
  }
  .card {
    position: relative; width: 560px; height: 320px;
    border-radius: 18px; overflow: hidden;
    box-shadow: 0 10px 28px rgba(15, 30, 60, 0.18);
  }

  /* Back of card */
  .card--back {
    background: linear-gradient(160deg, var(--navy-deep) 0%, var(--navy) 60%, #1d528f 100%);
  }
  .card--back .pattern-area {
    position: absolute; inset: 0;
    background: linear-gradient(160deg, rgba(41,169,225,0.10) 0%, rgba(41,169,225,0.02) 55%, rgba(41,169,225,0.14) 100%);
  }
  .card--back .brand {
    position: absolute; right: 70px; bottom: 96px;
    display: flex; align-items: center; gap: 12px;
  }
  .card--back .brand-dot {
    width: 40px; height: 40px; border-radius: 50%; background: var(--sky);
  }
  .card--back .brand-name {
    color: var(--paper); font-weight: 700; font-size: 20px; letter-spacing: 0.5px;
    white-space: nowrap;
  }

  /* Front of card */
  .card--front { background: var(--paper); }
  .card--front .swoosh { position: absolute; inset: 0; }
  .card--front .brand {
    position: absolute; left: 30px; top: 132px;
    display: flex; align-items: center; gap: 12px;
  }
  .card--front .brand-dot {
    width: 54px; height: 54px; border-radius: 50%; background: var(--sky); flex: none;
  }
  .card--front .brand-name {
    color: var(--navy); font-weight: 700; font-size: 22px; letter-spacing: 0.4px;
    white-space: nowrap;
  }
  .divider {
    position: absolute; left: 318px; top: 50px; width: 1px; height: 130px;
    background: var(--navy);
  }
  .contact {
    position: absolute; left: 336px; top: 42px; color: var(--ink);
  }
  .contact-name {
    font-weight: 800; font-size: 19px; letter-spacing: 0.6px; color: var(--navy); line-height: 1.1;
    white-space: nowrap;
  }
  .contact-name .surname { color: var(--sky); }
  .contact-title { font-size: 10.5px; font-weight: 500; margin-top: 2px; }
  .contact-address { font-size: 10.5px; line-height: 1.35; margin-top: 10px; }
  .contact-lines { list-style: none; margin-top: 9px; font-size: 10.5px; }
  .contact-lines li { display: flex; align-items: center; gap: 6px; line-height: 1.6; white-space: nowrap; }
  .contact-lines svg { width: 10px; height: 10px; flex: none; }
</style>
</head>
<body>
<main class="sheet">

  <section class="card card--front" aria-label="Card front">
    <svg class="swoosh" viewBox="0 0 560 320" aria-hidden="true">
      <path d="M0,285 Q330,265 560,190 L560,320 L0,320 Z" fill="var(--navy)"/>
      <path d="M170,278 Q360,256 560,174" fill="none" stroke="var(--sky)" stroke-width="5"/>
    </svg>

    <div class="brand">
      <span class="brand-dot"></span>
      <span class="brand-name">MARLOWE LAW</span>
    </div>

    <span class="divider"></span>

    <div class="contact">
      <h1 class="contact-name">DANIEL <span class="surname">REYES</span></h1>
      <p class="contact-title">Managing Director</p>
      <p class="contact-address">318 Harbor Avenue<br>Westbridge ON 4620</p>
      <ul class="contact-lines">
        <li>
          <svg viewBox="0 0 10 10"><path d="M2 1 L4 1 L4.6 3 L3.4 3.8 Q4.4 5.8 6.2 6.6 L7 5.4 L9 6 L9 8 Q9 9 8 9 Q1 8.6 1 2 Q1 1 2 1 Z" fill="var(--sky)"/></svg>
          (555) 310-4728
        </li>
        <li>
          <svg viewBox="0 0 10 10"><rect x="0.5" y="2" width="9" height="6.5" fill="var(--sky)"/><path d="M0.5 2 L5 5.6 L9.5 2" fill="none" stroke="#fff" stroke-width="0.9"/></svg>
          info@marlowelaw.com
        </li>
        <li>
          <svg viewBox="0 0 10 10"><circle cx="5" cy="5" r="4.3" fill="none" stroke="var(--sky)" stroke-width="1"/><ellipse cx="5" cy="5" rx="1.8" ry="4.3" fill="none" stroke="var(--sky)" stroke-width="0.8"/><path d="M0.8 5 H9.2" stroke="var(--sky)" stroke-width="0.8"/></svg>
          www.marlowelaw.com
        </li>
      </ul>
    </div>
  </section>

  <section class="card card--back" aria-label="Card back">
    <div class="pattern-area" role="img" aria-label="Repeating pattern of the firm's globe symbol in tonal blues"></div>
    <div class="brand">
      <span class="brand-dot"></span>
      <span class="brand-name">MARLOWE LAW</span>
    </div>
  </section>

</main>
</body>
</html>
```